bargainmentor.net - Podcast Guest Marketing E-Flyer PDF

Dear Designers:I am in need of an attractive and attention-getting layout and design for a three-page marketing flyer (commonly known as a media one sheet) that will be sent via e-mail, as PDF file, to various Podcast hosts to market me as a guest on their podcasts. I want the design of the document to "mirror" the design and branding on my parent bargainmentor.net website. I am providing ALL the edited and proofread copy and content - the designer just needs to create the design for this marketing document. I want an active PDF document and icons should be used for ConnectFolio, Phone, E-mail , and website- with hyperlinks that connect accordingly. I need a fast turnaround.
Updates

Dear Designers - instead of using the photo in the project file of me speaking to the audience for the banner image - I thought it would be a better idea to make this marketing piece specific to Podcast Hosts. Therefore, an image such as the one in the link below would be good to use for a banner image. https://www.pixtrove-example.net/gallery?topic=recording+booth+images&ref=qz7&view=grid&id=Kx93LmPwa2RtVbN8YcQdE4&w=1377&h=804#pic=vRmalqobet:

Target Market(s)

This PDF document will be sent to 650 Podcast hosts in North America via a broadcast e-mail.

Font styles to use
Sans Serif

Colors
ec1f27
ffffff
000000
333333
9d9d9d

Requirements
Must have
• A three-page layout that is easy to navigate in PDF form.
• Proper font styles and sizes for key emphasis areas on the document/
• Consistent branding to mirror my bargainmentor.net parent website
• Must be easy for people to read
• Attention-getting design elements and layout
• Professional and sophisticated design
• Icons for contact information
Should not have
• Should not be cluttered and junky-looking.
• Should not use small font sizes that makes it difficult to read.
• If Podcast hosts are interested in having me as a guest - they will read the content as required on three-pages

```html
<!DOCTYPE html>
<html lang="en">
<head>
<meta charset="utf-8">
<title>bargainmentor.net – Podcast Guest One Sheet</title>
<link href="https://fonts.googleapis.com/css2?family=Roboto:wght@400;500;700&family=Roboto+Condensed:wght@400;700&display=swap" rel="stylesheet">
<style>
:root{
  --red:#ec1f27;
  --white:#ffffff;
  --black:#000000;
  --ink:#333333;
  --grey:#9d9d9d;
  --stage:#dcdcde;
  --head:"Roboto",Arial,sans-serif;
  --body:"Roboto Condensed","Arial Narrow",sans-serif;
}
*{box-sizing:border-box;margin:0;padding:0}
html,body{width:1200px;height:1200px;overflow:hidden}
body{background:var(--stage);position:relative;font-family:var(--body);color:var(--ink)}
.sheet{position:absolute;background:var(--white);display:flex;flex-direction:column;box-shadow:6px 8px 14px rgba(0,0,0,.28)}
.sheet--one{left:411px;top:11px;width:447px;height:577px}
.sheet--two{left:160px;top:600px;width:450px;height:580px}
.sheet--three{left:634px;top:602px;width:448px;height:578px}

.masthead{height:69px;flex:none;display:flex;align-items:center;justify-content:space-between;padding:0 13px 0 20px}
.brand{display:flex;align-items:center;gap:6px;margin-top:6px}
.brand__mark{width:22px;height:22px;background:var(--red)}
.brand__name{font-family:var(--head);font-size:20px;font-weight:400;color:var(--ink);letter-spacing:-.3px}
.contacts{list-style:none;display:flex;flex-direction:column;gap:5px}
.contacts li{display:flex;align-items:center;gap:5px;font-size:7px;color:var(--black)}
.contacts svg{width:10px;height:10px;flex:none}

.band{flex:none}
.band--red{background:var(--red);color:var(--white)}
.band--black{background:var(--black);color:var(--white)}
.band--white{background:var(--white)}
.footer{height:34px;display:flex;align-items:center;justify-content:center;font-family:var(--head);font-weight:700;font-size:10.5px;letter-spacing:.8px;color:var(--white);background:var(--red);margin-top:auto}

.hero{height:110px;position:relative;background:var(--black);overflow:hidden}
.hero__photo{position:absolute;left:0;top:0;width:170px;height:110px;background:linear-gradient(110deg,#2a2a2a 0%,#6e6e6e 45%,#1a1a1a 80%,#000 100%)}
.hero__title{position:absolute;right:38px;top:22px;text-align:center;font-family:var(--head);font-weight:700;font-size:15.5px;line-height:17.5px;color:var(--white)}
.hero__title sup{font-size:7px}
.portrait{position:absolute;left:23px;top:126px;width:100px;height:100px;border-radius:50%;border:3px solid var(--white);background:radial-gradient(circle at 50% 40%,#bdbdbd 0%,#6d6d6d 55%,#2c2c2c 100%);z-index:2}
.pitch{height:52px;display:flex;align-items:center;justify-content:flex-end;padding-right:50px}
.pitch p{width:270px;text-align:center;font-family:var(--head);font-weight:500;font-size:9.2px;line-height:10.2px}

.section-title{font-family:var(--head);font-weight:700;text-align:center;color:var(--black)}
.copy{font-size:6.5px;line-height:8.2px;color:var(--black)}
.why{height:77px;padding:8px 20px 0}
.why .section-title{font-size:10.5px;line-height:10.5px;margin-bottom:6px}
.why .copy{text-align:center}

.reasons{height:235px;padding:10px 22px 0 27px}
.reasons h2{font-family:var(--head);font-weight:700;font-size:11.8px;color:var(--white);text-align:center;margin-bottom:14px}
.reasons ol{list-style:none;counter-reset:r}
.reasons li{counter-increment:r;position:relative;padding-left:7px;font-size:6.5px;line-height:8.8px;color:var(--white);margin-bottom:13px}
.reasons li::before{content:counter(r) ".";position:absolute;left:0}

.strip-title{height:43px;display:flex;align-items:center;justify-content:center;font-family:var(--head);font-weight:700;font-size:16.5px}
.benefit{height:116px;padding:14px 32px 0}
.benefit .copy{margin-bottom:9px;font-size:6.6px;line-height:9.8px}
.media{height:125px;text-align:center;padding-top:10px}
.media h2{font-family:var(--head);font-weight:500;font-size:16px}
.media p{font-size:6.8px;margin-top:5px}
.badges{display:flex;justify-content:center;gap:18px;margin-top:13px}
.badge{width:56px;height:56px;border-radius:50%}
.badge--red{background:#c8262b}.badge--navy{background:#1b4f8a}.badge--white{background:var(--white)}
.profit{height:191px;padding:10px 24px 0 25px}
.profit .section-title{font-weight:500;font-size:16px;line-height:18px;margin-bottom:11px}
.profit .lead{margin-bottom:11px}
.profit ol{list-style:none;counter-reset:p}
.profit li{counter-increment:p;position:relative;padding-left:7px;font-size:6.5px;line-height:10px;color:var(--black);margin-bottom:8px}
.profit li::before{content:counter(p) ".";position:absolute;left:0}

.quote-mark{font-family:Georgia,serif;font-weight:700;color:var(--red);font-size:30px;line-height:1;position:absolute}
.strip-title--small{height:40px;font-size:10.5px;line-height:12px;text-align:center}
.testimonial{height:115px;position:relative;padding:12px 38px 0 54px;text-align:center}
.testimonial .copy{font-size:6.6px;line-height:10.2px}
.attrib{font-size:6.6px;line-height:10.2px;margin-top:9px;color:var(--black);text-align:center}
.attendees{height:234px;position:relative;padding:10px 40px 0 50px;text-align:center}
.attendees h2{font-family:var(--head);font-weight:500;font-size:10.5px;line-height:13px;margin:0 -20px 12px}
.attendees .copy{color:var(--white);font-size:6.6px;line-height:10.2px}
.attendees .attrib{color:var(--white)}
.cta{display:inline-block;margin-top:10px;background:var(--red);color:var(--white);font-family:var(--head);font-weight:700;font-size:7.5px;padding:4px 17px}
.booking{height:86px;display:flex;align-items:center;padding:0 0 0 56px;gap:30px}
.booking__photo{width:57px;height:73px;background:linear-gradient(160deg,#9a9a9a,#3a3a3a);border:1px solid var(--grey);flex:none}
.booking__text{text-align:center}
.booking__text h2{font-family:var(--head);font-weight:700;font-size:13px;line-height:13px;color:var(--black)}
.booking__text h2 sup{font-size:6px}
.booking__text p{font-size:6.8px;line-height:10px;margin-top:5px;color:var(--black)}
</style>
</head>
<body>

<svg width="0" height="0" style="position:absolute" aria-hidden="true">
  <symbol id="icon-mail" viewBox="0 0 10 10"><circle cx="5" cy="5" r="5" fill="#ec1f27"/><rect x="2.4" y="3.2" width="5.2" height="3.6" fill="none" stroke="#fff" stroke-width=".7"/><path d="M2.4 3.2L5 5.3 7.6 3.2" fill="none" stroke="#fff" stroke-width=".7"/></symbol>
  <symbol id="icon-phone" viewBox="0 0 10 10"><circle cx="5" cy="5" r="5" fill="#ec1f27"/><path d="M3.2 2.5c.5-.3.8-.2 1 .2l.4.9c.1.3 0 .5-.2.7l-.3.3c.3.7.8 1.2 1.4 1.5l.3-.3c.2-.2.4-.3.7-.2l.9.4c.4.2.5.5.2 1-.4.6-1 .8-1.7.5C4.5 7 3.1 5.6 2.6 4.2c-.2-.6 0-1.3.6-1.7z" fill="#fff"/></symbol>
  <symbol id="icon-profile" viewBox="0 0 10 10"><circle cx="5" cy="5" r="5" fill="#ec1f27"/><circle cx="5" cy="3.8" r="1.3" fill="#fff"/><path d="M2.7 7.5c.4-1.3 1.2-1.9 2.3-1.9s1.9.6 2.3 1.9z" fill="#fff"/></symbol>
</svg>

<!-- Page one -->
<section class="sheet sheet--one">
  <header class="masthead">
    <div class="brand"><span class="brand__mark"></span><span class="brand__name">bargainmentor</span></div>
    <ul class="contacts">
      <li><svg><use href="#icon-mail"/></svg>daniel@varnek.com</li>
      <li><svg><use href="#icon-phone"/></svg>555-014-2287</li>
      <li><svg><use href="#icon-profile"/></svg>www.connectfolio.com/in/danielvarnek</li>
    </ul>
  </header>
  <div class="band hero">
    <div class="hero__photo" role="img" aria-label="Studio microphone in a podcast recording booth"></div>
    <h1 class="hero__title">Meet Bargain Mentor<sup>®</sup><br>Daniel R. Varnek<br>– The Expert You Need<br>As a Guest on Your Podcast</h1>
  </div>
  <div class="portrait" role="img" aria-label="Portrait of Daniel R. Varnek"></div>
  <div class="band band--red pitch">
    <p>Are you looking for a relevant and appealing topic and an engaging subject matter expert who can provide measurable value and life-changing tips to the listeners of your podcast?</p>
  </div>
  <div class="band band--white why">
    <h2 class="section-title">Why Negotiating and Decision Making Should Be<br>Topics on Your Podcast</h2>
    <p class="copy">Regardless of your podcast theme – it's important to remember that your listeners are negotiating all the time – in their personal lives, social lives, and especially in their business lives. Negotiating is an essential life skill. Everyone can improve his or her negotiating skills, and Daniel is the expert who can provide the answers your people crave. Your podcast listeners will benefit from Daniel's proven, practical, and relevant negotiating strategies and tips that will improve results and outcomes in all types of personal and business negotiations.</p>
  </div>
  <div class="band band--black reasons">
    <h2>Six Reasons to Book Daniel R. Varnek As a Guest on Your Podcast</h2>
    <ol>
      <li>Daniel is a dynamic, thought-provoking, engaging, captivating, and entertaining speaker who will share some great personal stories to help your listeners better understand and relate to the topic of negotiating and decision-making dynamics. He will indeed challenge the "status quo."</li>
      <li>Daniel is the founder of bargainmentor.net® and is an internationally recognized expert and highly rated speaker on the topics of negotiating and decision-making dynamics that affect negotiated outcomes. His versatility and commitment to proper preparation will ensure that his content is tailored to address the theme of your podcast and the needs of your listeners.</li>
      <li>His five-star-rated presentations and training programs have been delivered around the world to small and medium-sized businesses, leading global corporations, and large industry, trade, and peer-to-peer associations such as Rising Leaders Council and Founders Circle Network.</li>
      <li>Daniel has personally trained over 50,000 people of all experience levels, across multiple industries, in 31 countries how to negotiate more effectively.</li>
      <li>With formal training in broadcasting and media arts, Daniel provides 30 years of experience as a professional speaker who can provide your listeners with valuable insights, solutions, and answers to address listeners' challenges and questions.</li>
      <li>Daniel is the creator of the best-selling Deal Builder Toolkit Audio Learning Program – designed to be an effective all-in-one learning solution that helps people improve their negotiating capabilities and skills. He is also the host of his soon-to-be-launched Deal Talk Podcast.</li>
    </ol>
  </div>
  <footer class="footer">www.bargainmentor.net</footer>
</section>

<!-- Page two -->
<section class="sheet sheet--two">
  <header class="masthead">
    <div class="brand"><span class="brand__mark"></span><span class="brand__name">bargainmentor</span></div>
    <ul class="contacts">
      <li><svg><use href="#icon-mail"/></svg>daniel@varnek.com</li>
      <li><svg><use href="#icon-phone"/></svg>555-014-2287</li>
      <li><svg><use href="#icon-profile"/></svg>www.connectfolio.com/in/danielvarnek</li>
    </ul>
  </header>
  <h2 class="band band--red strip-title">How Podcast Listeners Will Benefit</h2>
  <div class="band band--white benefit">
    <p class="copy">Most people are intimidated by the prospect and process of negotiating – and often view negotiating as an uncomfortable haggling and bargaining process that may involve confrontation, anxiety, and stress. If podcast listeners are like most people – then they probably are concerned about being taken advantage of – or that they are missing out on potential opportunities in their personal, social, and business negotiations.</p>
    <p class="copy">To alleviate your listeners' concerns, Daniel will provide them with easy-to-understand negotiating strategies, tactics, phrases, and tips they can immediately apply – the moment the podcast episode ends. Your listeners will feel more confident when they are equipped with the powerful and beneficial strategies and techniques that will help them save/make money and arrive at better outcomes when negotiating with customers, clients, suppliers, contractors, financial institutions, retailers, co-workers, colleagues, and family members.</p>
  </div>
  <div class="band band--black media">
    <h2>Daniel R. Varnek in the Media</h2>
    <p>Daniel has appeared on radio programs, written articles or contributed to articles for the following media outlets:</p>
    <div class="badges">
      <span class="badge badge--red"></span><span class="badge badge--navy"></span><span class="badge badge--white"></span><span class="badge badge--white"></span><span class="badge badge--white"></span>
    </div>
  </div>
  <div class="band band--white profit">
    <h2 class="section-title">Three Ways You Can Profit From Booking<br>Daniel R. Varnek on Your Podcast</h2>
    <p class="copy lead">Upon mutual agreement, podcast hosts and listeners can have access to the following money-saving and profit-generating opportunities:</p>
    <ol>
      <li>Podcast hosts will be provided with a specific promotional code to share with your listeners that will entitle them to receive a special one-time discount of $19.95US off the purchase of the MP3 download of the Deal Builder Toolkit Audio Learning Program available on my online store. Complete download and purchase instructions will be provided to podcast hosts to publish in your notes and also communicate to your listeners.</li>
      <li>Podcast hosts will receive a 10% commission payable on the net sales dollar revenue generated from the sale of MP3 downloads of Daniel's Deal Builder Toolkit Audio Learning Program.</li>
      <li>Podcast hosts will receive a 10% referral fee for any corporation or association that books Daniel for a presentation, seminar, or learning workshop that directly results from my participation on your podcast.</li>
    </ol>
  </div>
  <footer class="footer">www.bargainmentor.net</footer>
</section>

<!-- Page three -->
<section class="sheet sheet--three">
  <header class="masthead">
    <div class="brand"><span class="brand__mark"></span><span class="brand__name">bargainmentor</span></div>
    <ul class="contacts">
      <li><svg><use href="#icon-mail"/></svg>daniel@varnek.com</li>
      <li><svg><use href="#icon-phone"/></svg>555-014-2287</li>
      <li><svg><use href="#icon-profile"/></svg>www.connectfolio.com/in/danielvarnek</li>
    </ul>
  </header>
  <h2 class="band band--red strip-title strip-title--small">Testimonials: What Some Clients Are Saying<br>About the Bargain Mentor®</h2>
  <div class="band band--white testimonial">
    <span class="quote-mark" style="left:32px;top:4px">“</span>
    <p class="copy">Daniel Varnek did a terrific job on my podcast. His negotiating insights and tips were well received by my listeners, and he was an engaging, knowledgeable, and entertaining guest. Given my expertise in real estate, I thought I was a good negotiator – until Daniel taught me a few new strategies and tips during the podcast. I would recommend Daniel to any podcast host – he is a pro and his topics are relevant and can benefit everyone.</p>
    <span class="quote-mark" style="right:24px;top:52px">”</span>
    <p class="attrib">Carl Whitmore<br>Podcast Host<br>Property Investor Roundtable Podcast, Austin, Texas</p>
  </div>
  <div class="band band--black attendees">
    <h2>Below is a partial listing of testimonials from attendees at<br>a Founders Circle Network (FCN) event provided by RT Halvorsen,<br>Chapter Learning Chair, FCN Western New York Chapter:</h2>
    <span class="quote-mark" style="left:28px;top:50px">“</span>
    <p class="copy">A very engaging, entertaining, and inspirational speaker who provided very useful information, strategies, and tips to apply to all my future negotiations."<br>"Thank you to FCN Western New York for booking this speaker! I learned some things that I can address immediately and a lot material that I need to practice. Great session!"<br>"Daniel was an outstanding speaker on the topic of negotiating! He was one of my favorite speakers ever! Daniel was a real 'teacher' versus other typical speakers who spend two hours bragging or promoting their book."<br>"Daniel was a very knowledgeable and well-prepared speaker who provided helpful tips and scripts throughout the entire presentation! I would love to learn more from this speaker.</p>
    <span class="quote-mark" style="right:24px;top:138px">”</span>
    <p class="attrib">RT Halvorsen, CEO and President<br>Northgate Records Services<br>Founders Circle Network (FCN) Western New York<br>Learning Chair</p>
    <span class="cta">Read More Testimonials - Click Here</span>
  </div>
  <div class="band band--white booking">
    <div class="booking__photo" role="img" aria-label="Portrait of Daniel R. Varnek"></div>
    <div class="booking__text">
      <h2>Book Bargain Mentor<sup>®</sup><br>Daniel R. Varnek for Your Podcast</h2>
      <p>E-mail: daniel@varnek.com<br>Phone: 555-014-2287<br>ConnectFolio Profile: connectfolio.com/in/danielvarnek</p>
    </div>
  </div>
  <footer class="footer">www.bargainmentor.net</footer>
</section>

</body>
</html>
```